Website homepage rework for women's travel website

I have a homepage (http://www.ladies-far-afield.example) that I'm 50% happy with but don't want to completely overhaul. I'd like to retain a similar look but upgrade it to something a bit more modern and less old-fashioned. The basic sense of the site is empowering, self-confident, fun and adventurous - but female and over 40.

A number of the elements on the page have to be redesigned, a few can be tweaked, and a few left alone. See the rest of the brief for further information.

Target Market(s)

women over 40 who like to travel

Industry/Entity Type

Travel

Number of Pages Required

1 page

Font styles to use
Other font styles liked:
• see my brief

Requirements
Must have
• - size - the page must be significantly wider
• - the only font I MUST keep is Raleway (as in the tagline) and possibly the font of the site name (Ladies Far Afield). Both of those work for me. There are too many fonts on the page, however, and that needs to be unified.
• - the rectangles I click to get inside the site have to change to something more modern, possibly square - they do not have to be separated into two columns as they are now, nor do they need the titles (toolkit etc)
• - I like the background image of the header - but it needs to be wider of course - also keep in mind the aspect - it has to fit into the smaller inside pages, whose size will not change
• - at the end of the project I need to receive the separate elements of the design so I can eventually make a change myself if needed ie. replace my own photo, for example
Nice to have
• - the three photos need to change to something more eye-popping - or something else should take their place to fill the space
Should not have
• I do not want a full, original redesign. I want my readers to still feel as though they are on the same site - same header, mostly same fonts.

```html
<!DOCTYPE html>
<html lang="en">
<head>
<meta charset="utf-8">
<title>Ladies Far Afield — For women who travel smart, safe + solo</title>
<link href="https://fonts.googleapis.com/css2?family=Cormorant+Garamond:ital,wght@1,500;1,600&family=Raleway:wght@400;500&display=swap" rel="stylesheet">
<style>
  :root {
    --ink: #2d2a2a;
    --white: #ffffff;
    --text: #333333;
    --line: #e4e4e4;
    --accent: #e8872a;
    --title-red: #d63a0a;
    --tile-red: #d9360b;
    --tile-purple: #9b59b6;
    --tile-copper: #d4814a;
    --tile-teal: #1ab394;
    --tile-crimson: #cc1e1e;
    --tile-blue: #3aa9ea;
    --tile-green: #14910f;
    --tile-amber: #e89612;
    --serif: 'Cormorant Garamond', Georgia, serif;
    --sans: 'Raleway', Arial, sans-serif;
    --edge: 20px;
    --content: 782px;
  }
  * { box-sizing: border-box; margin: 0; padding: 0; }
  html, body { width: 822px; height: 1200px; overflow: hidden; background: var(--white); }
  body { position: relative; font-family: var(--sans); color: var(--text); }
  a { text-decoration: none; }

  .site-nav {
    position: absolute; left: 0; top: 0; width: 822px; height: 38px;
    background: var(--ink); z-index: 3;
    display: flex; justify-content: center; gap: 40px; align-items: center;
  }
  .site-nav a { color: var(--white); font-size: 11.5px; letter-spacing: 0.3px; text-transform: uppercase; }

  .hero {
    position: absolute; left: 0; top: 38px; width: 822px; height: 300px;
    background: linear-gradient(180deg, #f0a024 0%, #f7c03a 45%, #e59a3a 70%, #b8623a 100%);
  }
  .hero-portrait {
    position: absolute; left: 50px; top: 30px; width: 300px; height: 270px;
    background: radial-gradient(ellipse at 50% 45%, #e8c6a8 0%, #cfae90 40%, #b9b39a 70%, rgba(200,180,140,0) 100%);
  }
  .site-title {
    position: absolute; left: 390px; top: 62px; width: 340px; height: 44px;
    background: linear-gradient(180deg, #e8501a, var(--title-red));
    color: var(--white); font-family: var(--serif); font-style: italic; font-weight: 500;
    font-size: 38px; line-height: 44px; text-align: center; white-space: nowrap;
  }
  .tagline {
    position: absolute; left: 390px; top: 110px; width: 340px;
    font-size: 17px; line-height: 22px; color: #3a2a1a; text-align: center;
    background: rgba(255,255,255,0.35); white-space: nowrap;
  }
  .snapshots { position: absolute; left: 412px; top: 142px; width: 300px; height: 110px; }
  .snap {
    position: absolute; width: 94px; height: 92px; background: var(--white);
    padding: 6px 6px 18px; box-shadow: 0 2px 5px rgba(0,0,0,0.35);
  }
  .snap span { display: block; width: 100%; height: 100%; }

  .intro-panel {
    position: absolute; left: var(--edge); top: 318px; width: var(--content); height: 20px; background: var(--white);
  }
  .greeting {
    position: absolute; left: 0; top: 346px; width: 822px; text-align: center;
    font-family: var(--serif); font-style: italic; font-weight: 500; font-size: 27px; line-height: 32px; color: var(--accent);
  }
  .greeting-sub {
    position: absolute; left: 0; top: 380px; width: 822px; text-align: center; font-size: 11px;
  }

  .promises {
    position: absolute; left: var(--edge); top: 412px; width: var(--content);
    display: grid; grid-template-columns: repeat(3, 1fr); gap: 12px;
  }
  .promise { position: relative; height: 104px; border: 1px solid var(--line); }
  .promise svg { position: absolute; left: 18px; top: 30px; }
  .promise h3 {
    position: absolute; left: 54px; top: 24px; font-family: var(--serif);
    font-style: italic; font-weight: 500; font-size: 19px; color: var(--ink);
  }
  .promise p { position: absolute; left: 54px; top: 52px; width: 180px; font-size: 10.5px; line-height: 14px; }

  .cta-band {
    position: absolute; left: var(--edge); top: 552px; width: var(--content); height: 58px;
    background: var(--ink); border-left: 3px solid var(--accent);
    color: var(--white); font-family: var(--serif); font-style: italic; font-weight: 500;
    font-size: 28px; line-height: 58px; text-align: center;
  }
  .cta-band s { text-decoration-thickness: 2px; }

  .tiles {
    position: absolute; left: var(--edge); top: 650px; width: var(--content);
    display: grid; grid-template-columns: repeat(4, 1fr); gap: 8px;
  }
  .tile { position: relative; height: 189.5px; overflow: hidden; }
  .tile-photo { position: absolute; inset: 0; }
  .tile-label { position: absolute; left: 0; width: 100%; padding: 10px 12px 11px 14px; color: var(--white); }
  .tile-label.top { top: 0; }
  .tile-label.bottom { bottom: 0; }
  .tile-label h4 { font-family: var(--serif); font-style: italic; font-weight: 600; font-size: 18px; line-height: 20px; }
  .tile-label p { font-size: 10px; line-height: 13px; margin-top: 2px; }

  .site-footer {
    position: absolute; left: 0; top: 1169px; width: 822px; height: 31px;
    background: var(--ink); color: var(--white); font-size: 9px; line-height: 31px; text-align: center;
  }
</style>
</head>
<body>

<nav class="site-nav">
  <a href="#">Start Here</a>
  <a href="#">About</a>
  <a href="#">Travel Resources</a>
  <a href="#">Blog</a>
  <a href="#">Travel Shop</a>
  <a href="#">Contact</a>
</nav>

<header class="hero" role="img" aria-label="Golden map background over a desert road with red mesas">
  <div class="hero-portrait" role="img" aria-label="Portrait of the site author smiling"></div>
  <h1 class="site-title">Ladies Far Afield</h1>
  <p class="tagline">For women who travel smart, safe + solo</p>
  <div class="snapshots">
    <div class="snap" style="left:0;top:8px;transform:rotate(-4deg)"><span role="img" aria-label="Beach with palm trees" style="background:linear-gradient(180deg,#7fc2e8,#2a7bb0 60%,#d9c49a)"></span></div>
    <div class="snap" style="left:102px;top:6px;transform:rotate(3deg)"><span role="img" aria-label="Blue planters with succulents" style="background:linear-gradient(180deg,#e9a26a,#3a9fd6 55%,#6e9a4a)"></span></div>
    <div class="snap" style="left:204px;top:0;transform:rotate(-3deg)"><span role="img" aria-label="Red scooter on a village street" style="background:linear-gradient(180deg,#c98f7a,#8aa86a 55%,#b0403a)"></span></div>
  </div>
</header>

<div class="intro-panel"></div>
<h2 class="greeting">Hi, I’m Maren</h2>
<p class="greeting-sub">I took my first solo trip at 15. I’ll show you how to travel…</p>

<div class="promises">
  <section class="promise">
    <svg width="26" height="26" viewBox="0 0 26 26" aria-hidden="true">
      <circle cx="8" cy="7" r="4" fill="#2d2a2a"/>
      <path d="M1 25 V15 a4 4 0 0 1 4-4 h6 a4 4 0 0 1 4 4 V25 Z" fill="#2d2a2a"/>
      <circle cx="20" cy="7" r="4" fill="#2d2a2a"/>
      <rect x="18" y="11" width="4" height="3" fill="#2d2a2a"/>
      <path d="M20 0 v1 M14 3 l1 1 M26 3 l-1 1" stroke="#2d2a2a" stroke-width="1.4"/>
    </svg>
    <h3>Smart:</h3>
    <p>practical tools to help you plan – and afford – the perfect trip</p>
  </section>
  <section class="promise">
    <svg width="22" height="26" viewBox="0 0 22 26" aria-hidden="true">
      <path d="M11 1 L20 4 V12 C20 19 15 23 11 25 C7 23 2 19 2 12 V4 Z" fill="none" stroke="#2d2a2a" stroke-width="2"/>
      <path d="M6.5 13 l3 3 l6-7" fill="none" stroke="#2d2a2a" stroke-width="2"/>
    </svg>
    <h3>Safe:</h3>
    <p>Down-to-earth advice and a ton of safety recommendations</p>
  </section>
  <section class="promise">
    <svg width="26" height="26" viewBox="0 0 26 26" aria-hidden="true">
      <circle cx="13" cy="13" r="12.5" fill="#111"/>
      <path d="M10 8 L14 6 V20" fill="none" stroke="#fff" stroke-width="3"/>
    </svg>
    <h3>Solo:</h3>
    <p>yes, you can do it!</p>
  </section>
</div>

<a class="cta-band" href="#">Thinking of solo travel? <s>Clickhere</s> to find out how.</a>

<div class="tiles">
  <a class="tile" href="#">
    <div class="tile-photo" style="background:linear-gradient(135deg,#f4efe8,#e9a07a 45%,#c7653a 70%,#f1ece4)" role="img" aria-label="Plate of smoked salmon and olives"></div>
    <div class="tile-label top" style="background:var(--tile-red)"><h4>Eating with locals</h4><p>The ultimate guide to social dining</p></div>
  </a>
  <a class="tile" href="#">
    <div class="tile-photo" style="background:linear-gradient(160deg,#8a8f95,#5a4a4a 45%,#8a2a30 70%,#3c4d8a)" role="img" aria-label="Travel gear laid out for packing"></div>
    <div class="tile-label bottom" style="background:var(--tile-purple)"><h4>Your Packing List</h4><p>Take what you need - no more</p></div>
  </a>
  <a class="tile" href="#">
    <div class="tile-photo" style="background:linear-gradient(160deg,#10162a,#1c3a8a 45%,#6fa0e0 60%,#141820)" role="img" aria-label="Cruise ship lit up at night"></div>
    <div class="tile-label top" style="background:var(--tile-copper)"><h4>No Single Supplement</h4><p>17 ways to avoid paying it</p></div>
  </a>
  <a class="tile" href="#">
    <div class="tile-photo" style="background:linear-gradient(135deg,#f2f0ec,#d8a25a 45%,#c07a34 65%,#eeece8)" role="img" aria-label="Plate of grilled fish fillets"></div>
    <div class="tile-label bottom" style="background:var(--tile-teal)"><h4>Europe For Foodies</h4><p>9 top destinations to try in October</p></div>
  </a>
  <a class="tile" href="#">
    <div class="tile-photo" style="background:linear-gradient(180deg,#9cc0dc,#d8d8d4 55%,#6f7a5e)" role="img" aria-label="Yurts on a grassy steppe by a lake"></div>
    <div class="tile-label bottom" style="background:var(--tile-crimson)"><h4>Solo Female Travel</h4><p>A 3-Week Central Asia itinerary</p></div>
  </a>
  <a class="tile" href="#">
    <div class="tile-photo" style="background:linear-gradient(90deg,#6e6e6e,#c8c8c8 45%,#e6e6e6 55%,#5a5a5a)" role="img" aria-label="Black and white photo of an old town street"></div>
    <div class="tile-label top" style="background:var(--tile-blue)"><h4>Rebellious Carouge</h4><p>Geneva’s Alter Ego?</p></div>
  </a>
  <a class="tile" href="#">
    <div class="tile-photo" style="background:linear-gradient(120deg,#cfc8bc,#8a8a8a 35%,#e6e2dc 55%,#7fb0a8)" role="img" aria-label="Shoes, guidebooks and travel documents laid out"></div>
    <div class="tile-label bottom" style="background:var(--tile-green)"><h4>Stress Management Courses</h4><p>How to travel stress-free</p></div>
  </a>
  <a class="tile" href="#">
    <div class="tile-photo" style="background:linear-gradient(180deg,#3a7ac0,#2a5a9a 50%,#1e4020 80%)" role="img" aria-label="Pine trees beside a blue mountain lake"></div>
    <div class="tile-label top" style="background:var(--tile-amber)"><h4>Solo In Argentina</h4><p>Does it really take two to tango</p></div>
  </a>
</div>

<footer class="site-footer">Copyright 2016 ladies-far-afield | All Right Reserved</footer>

</body>
</html>
```